New Business Card Design

we need a new business card as we have just moved location and need a fresh new look. we are a Land Surveying Company . the card needs to be 2 sided and needs to have what we do on the back as our previous card ( attached ).
i was thinking of maybe a ruler down the bottom of the card or something to make it stand out. size can be 90 x 55 or 90 x 45 .
maybe a shadow of the logo or something in the corner.
on the attached card where it says other offices , it should be Melbourne instead of bendigo

postal address should be there as PO box 318 , Tarrin Flats 3721
Updates

Project Deadline Extended
Reason: some designs didn't follow brief by having services provided on the back of the card, just giving a bit of time toi change and to review.

Industry/Entity Type

Business

Requirements
Must have
• All cards need to have services provided on the back please , as stated , a lot of designs have just had the logo on the back

```html
<!DOCTYPE html>
<html lang="en">
<head>
<meta charset="utf-8">
<title>Brannock Vale Land Surveyors – Business Card</title>
<link rel="stylesheet" href="https://fonts.googleapis.com/css2?family=Tinos:wght@400;700&display=swap">
<style>
  :root {
    --page-bg: #e9e6e1;
    --card-white: #ffffff;
    --card-blue: #87b1d8;
    --ink: #1c1c1c;
    --ink-soft: #7a7a7a;
    --rule-grey: #a7a9ac;
    --label-white: #ffffff;
    --brand-ink: #2b2b2b;
    --mark-blue: #1f66b3;
    --bullet-grey: #6d6f72;
  }
  * { margin: 0; padding: 0; box-sizing: border-box; }
  html, body { width: 1200px; height: 1000px; overflow: hidden; }
  body {
    position: relative;
    background: var(--page-bg);
    font-family: "Tinos", "Times New Roman", serif;
    color: var(--ink);
  }
  .card {
    position: absolute;
    box-shadow: 0 4px 14px rgba(0,0,0,0.35);
  }
  .card--front { left: 56px; top: 338px; width: 528px; height: 347px; background: var(--card-white); }
  .card--back  { left: 624px; top: 341px; width: 530px; height: 349px; background: var(--card-blue); }

  /* front: brand */
  .brand { position: absolute; left: 52px; top: 22px; display: flex; align-items: center; gap: 18px; }
  .brand__dot { width: 86px; height: 86px; border-radius: 50%; background: var(--mark-blue); }
  .brand__name {
    font-weight: 700; font-size: 31px; line-height: 1.08; letter-spacing: 1px;
    color: var(--brand-ink); text-transform: uppercase;
  }

  /* front: person */
  .person { position: absolute; left: 40px; top: 196px; }
  .person__name { font-size: 20px; line-height: 1.1; }
  .person__quals { font-size: 11px; color: var(--ink-soft); line-height: 1.2; margin-top: 3px; }
  .person__role { font-size: 14px; line-height: 1.05; margin-top: 2px; }

  /* front: contact panel */
  .contact-panel {
    position: absolute; left: 202px; top: 145px; width: 326px; height: 185px;
    background: var(--card-blue);
    border-top: 2px solid var(--rule-grey);
    border-bottom: 2px solid var(--rule-grey);
  }
  .contact-panel::before {
    content: ""; position: absolute; left: 0; right: 0; top: 3px; height: 1px; background: var(--rule-grey);
  }
  .address { position: absolute; left: 14px; top: 22px; font-size: 11.5px; line-height: 13.5px; }
  .contact-list { position: absolute; left: 14px; top: 95px; font-size: 11.5px; line-height: 13px; }
  .contact-list__row { display: flex; }
  .contact-list__label { width: 74px; color: var(--label-white); }

  /* back */
  .back-dot {
    position: absolute; left: 36px; top: 124px; width: 90px; height: 90px;
    border-radius: 50%; background: var(--mark-blue);
  }
  .services {
    position: absolute; left: 168px; top: 94px; padding-left: 24px;
    border-left: 2px dotted var(--card-white);
    font-size: 12px; line-height: 16.8px; height: 148px;
  }
  .services__list { list-style: none; }
  .services__item { position: relative; }
  .services__item::before {
    content: ""; position: absolute; left: -12px; top: 5px; width: 6px; height: 6px;
    border-radius: 50%; background: var(--bullet-grey);
  }
  .affiliations { margin-top: 8px; margin-left: 2px; font-size: 11.5px; line-height: 16.5px; }
</style>
</head>
<body>
  <section class="card card--front" aria-label="Business card front">
    <div class="brand">
      <span class="brand__dot"></span>
      <div class="brand__name">Brannock Vale<br>Land Surveyors</div>
    </div>

    <div class="person">
      <div class="person__name">Martin Keller</div>
      <div class="person__quals">B.App.Sci(Surv) MIS(Aust)<br>Grad.Dip.(Surv Prac)</div>
      <div class="person__role">Licensed Surveyor<br>Director</div>
    </div>

    <div class="contact-panel">
      <div class="address">
        Cnr Lindell Court and Marsh St.<br>
        Ashgrove East VIC 3561<br>
        PO box 318 , Tarrin Flats 3721
      </div>
      <div class="contact-list">
        <div class="contact-list__row"><span class="contact-list__label">Telephone:</span><span>03 5598 2140</span></div>
        <div class="contact-list__row"><span class="contact-list__label">Facsimile:</span><span>03 5598 2177</span></div>
        <div class="contact-list__row"><span class="contact-list__label">Mobile:</span><span>0412 630 958</span></div>
        <div class="contact-list__row"><span class="contact-list__label">Email:</span><span>martin@brannockvale.com.au</span></div>
        <div class="contact-list__row"><span class="contact-list__label">Website:</span><span>www.brannockvale.com.au</span></div>
      </div>
    </div>
  </section>

  <section class="card card--back" aria-label="Business card back">
    <span class="back-dot"></span>
    <div class="services">
      <ul class="services__list">
        <li class="services__item">Subdivision (Land Building)</li>
        <li class="services__item">Check Title Boundary Surveys</li>
        <li class="services__item">Features and Level Surveys</li>
        <li class="services__item">Neighbourhood &amp; Site Description PlanFor Development Permits</li>
        <li class="services__item">Town Planning State Design</li>
        <li class="services__item">Civil Engenniring Survey ( Roads, Structural &amp; Earthworks )</li>
      </ul>
      <div class="affiliations">
        Member of Survey Practitioners Guild<br>
        Member of Regional Land Development Council<br>
        Other Offices:&nbsp; Melbourne
      </div>
    </div>
  </section>
</body>
</html>
```